Full service meeting planning company needs new business cards

Velmora Linkway is a full service meeting planning company that specializes in on-line conference registration web development and event communications. We combine citywide hotel management, mobile applications, eblast reminders, confirmation letters, and customized reporting to create a seamless registration process. We also manage group motor coach transportation, food and beverages, entertainment, stage and lighting for group of 10 to 4000.

Target Market(s)

Corporations and associations

Industry/Entity Type

Event Planning

Contact Information for Business Card

standard size 3.5" wide and 2" tall

Font styles to use
Serif
Sans Serif

Colors
f37122
f78f20
333333
5c5c5c
9d9d9d
f68d4d

Requirements
Must have
• {name}
• Velmora Linkway
• P.O. Box 7384, Grand Rapids, M I 49568
• www.velmoralinkway.com
• {email}
• {phone}
• {mobile phone}
Nice to have
• Our colors are black, grey and orange as an accent color
Should not have
• I am not happy with our website layout anymore either. It feels dark and old but it does explain who we are pretty well if you'd like to review; www.velmoralinkway.com

```html
<!DOCTYPE html>
<html lang="en">
<head>
<meta charset="utf-8">
<title>Velmora Linkway – Business Card</title>
<link rel="stylesheet" href="https://fonts.googleapis.com/css2?family=Jost:wght@300;400;600&display=swap">
<style>
  :root {
    --backdrop: #e4e1dc;
    --card: #2c2c2c;
    --card-pattern: #313131;
    --ink: #ffffff;
    --ink-soft: #e8e8e8;
    --rule: #d9d9d9;
    --shadow: rgba(0, 0, 0, 0.25);
  }
  * { box-sizing: border-box; margin: 0; padding: 0; }
  html, body {
    width: 1200px; height: 987px; overflow: hidden;
    background: var(--backdrop);
    font-family: "Jost", "Futura", sans-serif;
  }
  .canvas { position: relative; width: 1200px; height: 987px; }
  .card {
    position: absolute; left: 293px; width: 615px; height: 352px;
    background: var(--card); color: var(--ink);
    box-shadow: 0 3px 10px var(--shadow);
  }
  .card--front { top: 130px; }
  .card--back { top: 505px; }

  .brand-name {
    position: absolute; right: 34px; top: 38px;
    font-weight: 600; font-size: 26px; letter-spacing: 0.2px;
  }
  .person { position: absolute; left: 28px; top: 140px; }
  .person__name { font-weight: 600; font-size: 22px; line-height: 1.1; letter-spacing: 0.3px; }
  .person__title { font-weight: 300; font-size: 17px; line-height: 1.3; color: var(--ink-soft); }
  .divider {
    position: absolute; left: 28px; width: 560px; top: 206px;
    height: 1px; background: var(--rule);
  }
  .contacts { position: absolute; left: 28px; top: 219px; list-style: none; }
  .contacts li {
    display: flex; align-items: center; gap: 7px;
    font-weight: 300; font-size: 17.5px; line-height: 24.5px; color: var(--ink-soft);
  }
  .contacts svg { width: 14px; height: 14px; fill: var(--ink); flex: none; }
  .address {
    position: absolute; right: 26px; top: 222px; text-align: right;
    font-style: normal; font-weight: 300; font-size: 17.5px; line-height: 22.5px; color: var(--ink-soft);
  }
  .edge-band { position: absolute; left: 0; right: 0; background: var(--ink); }
  .edge-band--thin { top: 334px; height: 3px; }
  .edge-band--thick { top: 341px; height: 11px; }

  .back-pattern {
    position: absolute; inset: 0;
    background: linear-gradient(180deg, var(--card-pattern), var(--card));
  }
  .back-mark {
    position: absolute; right: 75px; top: 254px;
    display: flex; align-items: center; gap: 12px;
  }
  .back-mark__name { font-weight: 600; font-size: 18px; color: var(--ink); }
  .back-mark__dot { width: 60px; height: 60px; border-radius: 50%; background: var(--ink); }
</style>
</head>
<body>
<main class="canvas">
  <section class="card card--front">
    <h1 class="brand-name">VELMORA LINKWAY</h1>
    <div class="person">
      <p class="person__name">DANA WHITFIELD</p>
      <p class="person__title">CEO/FOUNDER</p>
    </div>
    <div class="divider"></div>
    <ul class="contacts">
      <li><svg viewBox="0 0 16 16"><path d="M3.6 1.2l2.3 2.9-1.3 1.8c.9 2 2.5 3.6 4.5 4.5l1.8-1.3 2.9 2.3-1.4 2.4C7.2 13.6 2.4 8.8 1.2 2.6z"/></svg>(616) 555-0148</li>
      <li><svg viewBox="0 0 16 16"><path d="M4 0h8v16H4zM5.5 2v10h5V2zM8 13a1 1 0 100 2 1 1 0 000-2z" fill-rule="evenodd"/></svg>(836) 555-0172</li>
      <li><svg viewBox="0 0 16 16"><path d="M1 4h14v1L8 9.5 1 5zM1 6.5l7 4.5 7-4.5V13H1z"/></svg>dana@velmoralinkway.com</li>
      <li><svg viewBox="0 0 16 16"><path d="M8 1a7 7 0 100 14A7 7 0 008 1zm-1 2.2c-.4 1 .6 1.6 1.4 2 .9.5.3 1.6-.6 1.5-1.2-.2-2.1.6-1.8 1.8.3 1 1.5 1 1.6 2.2.1.9-.5 1.8-.3 2.6A5.4 5.4 0 017 3.2zm4.2 1.3a5.4 5.4 0 011.8 6.2c-.7-.6-1.3-1.7-.8-2.7.5-1-1.3-1.2-1.2-2.2 0-.6.3-1 .2-1.3z"/></svg>www.velmoralinkway.com</li>
    </ul>
    <address class="address">
      Velmora Linkway<br>
      P.O. Box 7384<br>
      Grand Rapids, M I 49568
    </address>
    <div class="edge-band edge-band--thin"></div>
    <div class="edge-band edge-band--thick"></div>
  </section>

  <section class="card card--back">
    <div class="back-pattern" role="img" aria-label="Faint repeating brand pattern across the card back"></div>
    <div class="back-mark">
      <span class="back-mark__name">Velmora Linkway</span>
      <span class="back-mark__dot"></span>
    </div>
  </section>
</main>
</body>
</html>
```